Financial Services Consultant needs a business card

We need a business card for a new consulting company based in Melbourne called
"Korvane Metrics". Tagline is Measure, Monitor, Save
We would like to see business card designs that are in line with the minimal style of the website www.korvane-metrics-example.com
The font I have used on the website is Proxima Nova and would like the same or similar font used on the business card with a minimal design in line with the website Two sided with "KORVANE METRICS" MEASURE, MONITOR, SAVE on one side and name, title and contact details on the otther
Updates

Hi All, thanks for your submissions, much appreciated.

I have recently added some colour to my webiste, it is hex #3a7b74 for those that wish to use it
Thanks

Hi all

thanks very much for your design submissions I am very impressed and they are much appreciated.

Interms of general feedback please find below;

Colour: I am trying to stick to a minimal design and colour scheme for my website which is still under construction, up to 3 colours( www.korvane-metrics-example.com) it is currently black and white with a small amount of blue/green but I am open to suggestion/interpretations for a consulting company.

Card: I dont mind if it has rounded edges or straight, I was thinking about using a letterpress card if possible

Detail: the detail on the card will include; Name, Title, Mobile, Personal Email, Business Email,Web,Business Address

Once again thanks for submissions

Industry/Entity Type

Business

```html
<!DOCTYPE html>
<html lang="en">
<head>
<meta charset="utf-8">
<title>Korvane Metrics – Business Card</title>
<link rel="stylesheet" href="https://fonts.googleapis.com/css2?family=Figtree:wght@300;400;700&display=swap">
<style>
  :root {
    --page-bg: #ffffff;
    --card-bg: #ffffff;
    --card-edge: #8a8a8a;
    --card-shadow: #cfcfcf;
    --brand-green: #2f8f63;
    --ink: #111111;
  }
  html, body {
    margin: 0;
    padding: 0;
    width: 1200px;
    height: 1000px;
    overflow: hidden;
    background: var(--page-bg);
    font-family: "Figtree", "Helvetica Neue", Arial, sans-serif;
  }
  .canvas {
    position: relative;
    width: 1200px;
    height: 1000px;
  }
  .card-shadow {
    position: absolute;
    left: 86px;
    top: 213px;
    width: 1050px;
    height: 600px;
    background: var(--card-shadow);
    filter: blur(3px);
  }
  .card {
    position: absolute;
    left: 76px;
    top: 201px;
    width: 1050px;
    height: 600px;
    box-sizing: border-box;
    background: var(--card-bg);
    border: 1px solid var(--card-edge);
    overflow: hidden;
  }
  .divider {
    position: absolute;
    top: 0;
    bottom: 0;
    width: 2px;
    background: var(--brand-green);
  }
  .divider--left { left: 304px; }
  .divider--right { left: 914px; }

  .identity {
    position: absolute;
    left: 158px;
    top: 551px;
    transform-origin: 0 0;
    transform: rotate(-90deg);
    white-space: nowrap;
    font-size: 49px;
    line-height: 56px;
  }
  .identity__name {
    display: block;
    font-weight: 700;
    color: var(--brand-green);
  }
  .identity__title {
    display: block;
    font-weight: 400;
    color: var(--ink);
  }

  .contact {
    position: absolute;
    left: 376px;
    top: 0;
    width: 520px;
    height: 100%;
  }
  .address {
    position: absolute;
    top: 119px;
    margin: 0;
    font-style: normal;
    font-weight: 300;
    font-size: 39px;
    line-height: 50px;
    color: var(--brand-green);
    white-space: nowrap;
  }
  .details {
    position: absolute;
    top: 270px;
    margin: 0;
    padding: 0;
    list-style: none;
    font-size: 35px;
    line-height: 46px;
    white-space: nowrap;
  }
  .details__label {
    font-weight: 700;
    color: var(--brand-green);
    margin-right: 10px;
  }
  .details__value {
    font-weight: 400;
    color: var(--ink);
  }
  .website {
    position: absolute;
    top: 515px;
    margin: 0;
    font-weight: 700;
    font-size: 30px;
    letter-spacing: -0.2px;
    color: var(--brand-green);
    white-space: nowrap;
  }
</style>
</head>
<body>
  <div class="canvas">
    <div class="card-shadow"></div>
    <section class="card" aria-label="Korvane Metrics business card, contact side">
      <div class="divider divider--left"></div>
      <div class="divider divider--right"></div>

      <div class="identity">
        <span class="identity__name">Elan Marsh</span>
        <span class="identity__title">Marketing Manager</span>
      </div>

      <div class="contact">
        <address class="address">123 Somewhere Lane<br>City, State, 12345</address>
        <ul class="details">
          <li><span class="details__label">Phone/</span> <span class="details__value">555·555·5555</span></li>
          <li><span class="details__label">Fax/</span> <span class="details__value">555·555·5555</span></li>
          <li><span class="details__label">E-mail/</span><span class="details__value">elan@kmetrics.example</span></li>
        </ul>
        <p class="website">www.korvane-metrics-example.com</p>
      </div>
    </section>
  </div>
</body>
</html>
```